Harborline Motors LLC

Car Dealer Customer Service
Address: 2741 Linden Avenue, Shelbyville, TN 37162
web: www.harborlinemotorstn.net
email: harborlinemotorstn@mailbox-example.net
Phone: (931) 555-0148
Phone: (629) 555-0173

```html
<!DOCTYPE html>
<html lang="en">
<head>
<meta charset="utf-8">
<title>Harborline Motors — Business Card</title>
<link rel="stylesheet" href="https://fonts.googleapis.com/css2?family=Figtree:wght@600;800&display=swap">
<style>
  :root {
    --brand-blue: #0e87b6;
    --band-blue: #0aa3d6;
    --sky: #9dd2ea;
    --sand: #f8deb2;
    --gold: #f2c063;
    --card-edge: #e4e4e4;
    --page: #ffffff;
  }
  * { box-sizing: border-box; margin: 0; padding: 0; }
  html, body {
    width: 1200px; height: 1000px; overflow: hidden;
    background: var(--page);
    font-family: "Figtree", Arial, sans-serif;
  }
  .card {
    position: absolute; left: 205px; width: 792px; height: 440px;
    border: 1px solid var(--card-edge); background: #fff; overflow: hidden;
  }
  .card--front { top: 30px; }
  .card--back { top: 501px; }

  .front-artwork {
    position: absolute; inset: 0;
    background: linear-gradient(120deg, var(--sky) 0%, #cfe6ef 35%, var(--sand) 60%, #fbe8c8 100%);
  }
  .brand-mark {
    position: absolute; left: 50%; transform: translateX(-50%);
    border-radius: 50%; background: var(--band-blue);
  }
  .card--front .brand-mark { top: 135px; width: 130px; height: 130px; }
  .card--back .brand-mark { top: 62px; width: 100px; height: 100px; }

  .brand-name {
    position: absolute; left: 0; right: 0; text-align: center;
    color: var(--brand-blue); font-weight: 800; letter-spacing: 0.5px;
    text-transform: uppercase;
  }
  .card--front .brand-name { top: 278px; font-size: 31px; }
  .card--back .brand-name { top: 168px; font-size: 25px; }

  .web-address {
    position: absolute; top: 327px; left: 0; right: 0; text-align: center;
    color: var(--brand-blue); font-weight: 600; font-size: 18px; letter-spacing: 1.5px;
  }

  .contact-list { position: absolute; left: 158px; top: 243px; list-style: none; }
  .contact-item {
    display: flex; align-items: center; height: 48px;
    color: var(--brand-blue); font-weight: 600; font-size: 21px;
  }
  .contact-icon { width: 18px; height: 18px; margin-right: 16px; flex: none; }

  .footer-band { position: absolute; bottom: 0; height: 35px; width: 50%; }
  .footer-band--gold { left: 0; background: var(--gold); }
  .footer-band--blue { right: 0; background: var(--band-blue); }
</style>
</head>
<body>

<section class="card card--front">
  <div class="front-artwork" role="img" aria-label="Diagonal pattern of light blue and sand horizontal stripes"></div>
  <div class="brand-mark"></div>
  <h1 class="brand-name">Harborline Motors</h1>
  <p class="web-address">www.harborlinemotorstn.net</p>
</section>

<section class="card card--back">
  <div class="brand-mark"></div>
  <h2 class="brand-name">Harborline Motors</h2>
  <ul class="contact-list">
    <li class="contact-item">
      <svg class="contact-icon" viewBox="0 0 24 24" aria-hidden="true"><path fill="#f2c063" d="M6.6 10.8a15.1 15.1 0 0 0 6.6 6.6l2.2-2.2a1 1 0 0 1 1-.25 11.4 11.4 0 0 0 3.6.57 1 1 0 0 1 1 1V20a1 1 0 0 1-1 1A17 17 0 0 1 3 4a1 1 0 0 1 1-1h3.5a1 1 0 0 1 1 1c0 1.25.2 2.45.57 3.6a1 1 0 0 1-.25 1z"/></svg>
      (931) 555-0148 \ (629) 555-0173
    </li>
    <li class="contact-item">
      <svg class="contact-icon" viewBox="0 0 24 24" aria-hidden="true"><rect x="2" y="5" width="20" height="14" fill="#f2c063"/><path d="M2 5l10 8 10-8" fill="none" stroke="#fff" stroke-width="1.5"/></svg>
      harborlinemotorstn@mailbox-example.net
    </li>
    <li class="contact-item">
      <svg class="contact-icon" viewBox="0 0 24 24" aria-hidden="true"><path fill="#f2c063" d="M12 3l9 7v11h-6v-6H9v6H3V10z"/></svg>
      2741 Linden Avenue, Shelbyville, TN 37162
    </li>
  </ul>
  <div class="footer-band footer-band--gold"></div>
  <div class="footer-band footer-band--blue"></div>
</section>

</body>
</html>
```